Modern Label for Loose Tea pouches on 4.5x6 Label

We need a new label for our teas that is very simple in design, but stylish and modern. This will be used to print labels for our loose tea pouches. The label will be at max 4.5x6 inches in size. There should be a place for the tea name, description, ingredients, and size that is changeable.
Preferably an AI file that allows me to setup variables to change the above items. There will also need to be our logo which is supplied, and our address on the label.
Address:
Brindle Teas
148 Lower Ferncliff Lane
Brenwick, OR 97012
Target Market(s)
Tea Lovers
Requirements
Must have
- Adobe Illustrator file with variables setup for replacement of tea name, description, ingredients, and size (weights 2oz, 4oz, 8oz, 1lb)

```html
<!DOCTYPE html>
<html lang="en">
<head>
<meta charset="utf-8">
<title>Good Morning – Tea Pouch Label</title>
<link rel="stylesheet" href="https://fonts.googleapis.com/css2?family=Fira+Sans:wght@300;400&family=Open+Sans:wght@400;700&display=swap">
<style>
  :root {
    --pink: #d9589c;
    --green: #b9d540;
    --charcoal: #39383b;
    --ink: #2e2e2e;
    --paper: #ffffff;
    --edge: #dcdcdc;
    --backdrop: #f4f4f4;
  }
  * { box-sizing: border-box; margin: 0; padding: 0; }
  html, body {
    width: 868px;
    height: 1200px;
    overflow: hidden;
    background: var(--backdrop);
  }
  .label {
    position: absolute;
    left: 24px;
    top: 53px;
    width: 820px;
    height: 1093px;
    background: var(--paper);
    border: 1px solid var(--edge);
    font-family: "Open Sans", sans-serif;
    color: var(--ink);
  }
  .side-band {
    position: absolute;
    left: 25px;
    top: 23px;
    width: 242px;
    height: 854px;
    background: var(--pink);
    overflow: hidden;
  }
  .leaf-art {
    position: absolute;
    inset: 0;
    background: linear-gradient(180deg, rgba(255,255,255,0) 5%, rgba(255,255,255,0.22) 50%, rgba(255,255,255,0) 95%);
  }
  .brand {
    position: absolute;
    left: 267px;
    width: 553px;
    top: 215px;
    text-align: center;
    font-family: "Fira Sans", sans-serif;
    font-weight: 400;
    font-size: 52px;
    letter-spacing: 2px;
    color: var(--green);
  }
  .tea-name {
    position: absolute;
    left: 267px;
    width: 553px;
    top: 305px;
    text-align: center;
    font-family: "Fira Sans", sans-serif;
    font-weight: 300;
    font-size: 76px;
    line-height: 1.02;
    color: var(--ink);
  }
  .size-pill {
    position: absolute;
    left: 480px;
    top: 497px;
    width: 137px;
    height: 60px;
    border-radius: 50%;
    background: var(--green);
    color: var(--paper);
    font-family: "Fira Sans", sans-serif;
    font-weight: 300;
    font-size: 36px;
    line-height: 60px;
    text-align: center;
  }
  .section-title {
    font-family: "Fira Sans", sans-serif;
    font-weight: 300;
    font-size: 46px;
    line-height: 1;
  }
  .description {
    position: absolute;
    left: 312px;
    top: 620px;
    width: 490px;
  }
  .description .section-title { color: var(--pink); margin-bottom: 22px; }
  .description p { font-size: 20.5px; line-height: 29px; }
  .address-box {
    position: absolute;
    left: 25px;
    top: 877px;
    width: 242px;
    height: 190px;
    background: var(--green);
    padding: 20px 0 0 25px;
  }
  .address-box .section-title { color: var(--charcoal); margin-bottom: 26px; }
  .address-box address {
    font-style: normal;
    font-weight: 700;
    font-size: 15.5px;
    line-height: 22px;
    white-space: nowrap;
    color: var(--charcoal);
  }
  .ingredients-box {
    position: absolute;
    left: 267px;
    top: 877px;
    width: 518px;
    height: 190px;
    background: var(--charcoal);
    color: var(--paper);
    padding: 20px 0 0 48px;
  }
  .ingredients-box .section-title { margin-bottom: 22px; }
  .ingredients-box p { font-size: 20.5px; line-height: 27px; }
</style>
</head>
<body>
  <div class="label">
    <div class="side-band">
      <div class="leaf-art" role="img" aria-label="White line illustration of a tea leaf sprig"></div>
    </div>

    <div class="brand">BRINDLE TEAS</div>

    <h1 class="tea-name">Good<br>Morning</h1>
    <div class="size-pill">2oz</div>

    <section class="description">
      <h2 class="section-title">Descriptions:</h2>
      <p>Smooth and sublime, this organic rare white tea is enlivened with crisp apples and the flavor of sun-sweet tangerines. An alluring addition of fragrant rosemary adds to this savory garden cup. Refreshing iced!</p>
    </section>

    <section class="address-box">
      <h2 class="section-title">Address:</h2>
      <address>Brindle Teas<br>148 Lower Ferncliff Lane<br>Brenwick, OR 97012</address>
    </section>

    <section class="ingredients-box">
      <h2 class="section-title">Ingridients:</h2>
      <p>Sena Leaf, Bukthorn Bar, Fannel Seed,<br>Chamomile, Pepermint, Cinamon Bark</p>
    </section>
  </div>
</body>
</html>
```